Card for invoking rights with police

Our criminal defense law firm is seeking proposals for a design for our card intended for clients to carry with them in their car. Upon being pulled over, they would hand this card to the officer.
Text for the back of the card:
"For Law Enforcement:"
"I will comply with lawful orders but respectfully decline any test or other requests without my attorney. I wish to remain silent, do not consent to searches, and request to speak with my attorney now.
The back of the card should prominently feature the text and the firm logo should be secondary.
Front
Must prominently feature contact info: 503-555-0182. Do not include attorney name, email, phone from the example file. This is intended to be generic for the firm and not tied to an individual lawyer.
Included for design reference: current business card, firm logo.
We intend to use trenvo.com to produce the cards.
Updates
The back of the card should prominently display the text regarding invocation of rights. Please title it "For Law Enforcement".
Target Market(s)
People who have been stopped by police
Contact Information for Business Card
see project description
Look and feel

```html
<!DOCTYPE html>
<html lang="en">
<head>
<meta charset="utf-8">
<title>Varden Law Firm – Rights Card</title>
<link rel="stylesheet" href="https://fonts.googleapis.com/css2?family=Montserrat:wght@300;400;700&family=Open+Sans:wght@400&display=swap">
<style>
  :root {
    --page: #ecedef;
    --navy: #0b2e4f;
    --navy-band: rgba(255, 255, 255, 0.045);
    --white: #ffffff;
    --paper-band: rgba(0, 0, 0, 0.035);
    --divider-dark: rgba(255, 255, 255, 0.35);
    --divider-light: rgba(11, 46, 79, 0.35);
  }
  * { box-sizing: border-box; margin: 0; padding: 0; }
  html, body {
    width: 1029px; height: 1200px; overflow: hidden;
    background: var(--page);
  }
  .sheet {
    width: 1029px; height: 1200px;
    display: flex; flex-direction: column; align-items: center; justify-content: center;
    gap: 70px;
  }
  .card {
    position: relative;
    width: 620px; height: 354px;
    box-shadow: 0 6px 16px rgba(0, 0, 0, 0.18);
    overflow: hidden;
  }

  /* Shared brand block */
  .brand {
    position: absolute;
    display: flex; align-items: center; gap: 12px;
  }
  .brand__square {
    flex: none;
    width: 24px; height: 24px; background: currentColor;
  }
  .brand__name {
    font-family: "Montserrat", sans-serif; font-weight: 400;
    font-size: 17px; line-height: 1.25;
    letter-spacing: 0.18em; text-transform: uppercase;
  }
  .brand__name span { display: block; }

  /* Front */
  .card--front {
    background:
      linear-gradient(120deg, transparent 28%, var(--navy-band) 28%, var(--navy-band) 40%, transparent 40%),
      linear-gradient(120deg, transparent 52%, var(--navy-band) 52%, var(--navy-band) 66%, transparent 66%),
      var(--navy);
    color: var(--white);
  }
  .front__brand { left: 60px; top: 142px; }
  .front__divider {
    position: absolute; left: 255px; top: 58px; width: 1px; height: 210px;
    background: var(--divider-dark);
  }
  .front__icon {
    position: absolute; left: 400px; top: 78px; width: 68px; height: 68px;
  }
  .front__phone {
    position: absolute; left: 278px; top: 168px; width: 312px;
    text-align: center;
    font-family: "Montserrat", sans-serif; font-weight: 300;
    font-size: 40px; letter-spacing: 0.02em;
  }
  .front__web {
    position: absolute; left: 0; right: 0; bottom: 40px;
    text-align: center;
    font-family: "Montserrat", sans-serif; font-weight: 400; font-size: 17px;
  }

  /* Back */
  .card--back {
    background:
      linear-gradient(125deg, transparent 22%, var(--paper-band) 22%, var(--paper-band) 34%, transparent 34%),
      linear-gradient(125deg, transparent 44%, var(--paper-band) 44%, var(--paper-band) 54%, transparent 54%),
      linear-gradient(125deg, transparent 70%, var(--paper-band) 70%, var(--paper-band) 80%, transparent 80%),
      var(--white);
    color: var(--navy);
  }
  .back__title {
    position: absolute; left: 48px; top: 140px;
    font-family: "Montserrat", sans-serif; font-weight: 700;
    font-size: 21px; line-height: 1.0; text-transform: uppercase;
  }
  .back__divider {
    position: absolute; left: 236px; top: 48px; width: 1px; height: 215px;
    background: var(--divider-light);
  }
  .back__statement {
    position: absolute; left: 262px; top: 50px; width: 310px;
    font-family: "Open Sans", sans-serif; font-weight: 400;
    font-size: 17px; line-height: 1.6;
  }
  .back__brand { left: 262px; top: 282px; gap: 10px; }
  .back__brand .brand__square { width: 22px; height: 22px; }
  .back__brand .brand__name { font-size: 15px; }
</style>
</head>
<body>
<main class="sheet">
  <section class="card card--front" aria-label="Card front">
    <div class="brand front__brand">
      <span class="brand__square"></span>
      <span class="brand__name"><span>Varden</span><span>Law Firm</span></span>
    </div>
    <div class="front__divider"></div>
    <svg class="front__icon" viewBox="0 0 68 68" aria-label="Phone">
      <circle cx="34" cy="34" r="34" fill="#ffffff"/>
      <path d="M25 19c2-1 3 0 4 2l3 6c1 2 0 3-1 4l-2 2c1 4 4 7 8 9l2-2c1-1 2-2 4-1l6 3c2 1 2 3 1 4l-2 3c-2 2-5 3-9 1-7-3-13-9-16-16-2-5-1-8 2-10z" fill="#0b2e4f"/>
      <path d="M38 22a9 9 0 0 1 8 8M39 16a15 15 0 0 1 13 13M40 10a21 21 0 0 1 18 18" stroke="#0b2e4f" stroke-width="2" fill="none" stroke-linecap="round"/>
    </svg>
    <p class="front__phone">503-555-0182</p>
    <p class="front__web">www.vardenlawfirm.com</p>
  </section>

  <section class="card card--back" aria-label="Card back">
    <h1 class="back__title">For Law<br>Enforcement</h1>
    <div class="back__divider"></div>
    <p class="back__statement">I will comply with lawful orders but respectfully decline any test or other requests without my attorney. I wish to remain silent, do not consent to searches, and request to speak with my attorney now.</p>
    <div class="brand back__brand">
      <span class="brand__square"></span>
      <span class="brand__name">Varden Law Firm</span>
    </div>
  </section>
</main>
</body>
</html>
```